We need a nice multi-page site that is new cutting edge and reflect who we are in Miami Beach and the world.

We have an existing site and we need to make the new one more user friendly, video uploads, word press base, nice soft touch with our logo, sexy look

Present site www.brenvitale-example.com

Target Market(s)

Upscale high end demographic traveling to and from Miami Beach

Industry/Entity Type

Clinic

Requirements
Must have
• 1) Very Refined elegant site, clean ...Corvalinesq...www.corvaline-example.com...www.marrowby-example.com..Logo in middle of page, nice placed and drop-down toward the sides
2) Very visual and inviting
3) We need to tell the story of our health care model, Dr Tobias Brenwick traveling around the world bringing back to BVC, a unique holistic health care model based on three main points....we can get into that later
4) Contact us call to action button
5) Newsletter option
6) E-commerce section
Should not have
• Not too cheeky, not canned, button and boxes off the shelf

```html
<!DOCTYPE html>
<html lang="en">
<head>
<meta charset="utf-8">
<title>Brenwick Vitality Clinic</title>
<link href="https://fonts.googleapis.com/css2?family=Source+Sans+3:ital,wght@0,400;0,600;0,700;1,400&display=swap" rel="stylesheet">
<style>
:root{
  --page-bg:#476c92;
  --brand:#4a6d93;
  --nav-top:#6490bb;
  --nav-bottom:#3e668f;
  --ink:#3b3b3b;
  --muted:#6b6b6b;
  --panel:#ffffff;
  --strip:#f1f1f1;
  --dark-band:#393939;
  --footer:#434343;
}
*{box-sizing:border-box;margin:0;padding:0}
html,body{width:1200px;height:1148px;overflow:hidden;background:var(--page-bg)}
body{font-family:"Source Sans 3",sans-serif;color:var(--ink)}
.stage{position:absolute;left:0;top:0;width:1150px;height:1100px;transform:scale(1.0435);transform-origin:0 0}
.abs{position:absolute}

.search{left:898px;top:14px;width:164px;height:23px;border-radius:12px;background:#fff;border:1px solid #c9d3de;font-size:11px;font-style:italic;color:#9a9a9a;padding:4px 0 0 17px}
.search svg{position:absolute;right:12px;top:6px}

.sheet{left:90px;top:50px;width:972px;height:1000px;background:var(--panel)}

.brand-name{left:164px;top:106px;font-size:24px;letter-spacing:.5px;color:var(--brand);font-weight:400;display:flex;align-items:center;gap:10px}
.brand-name .dot{width:14px;height:14px;border-radius:50%;background:var(--brand)}

.call-icon{left:752px;top:70px}
.contact-block{right:100px;top:64px;text-align:right;white-space:nowrap}
.call{font-size:27px;line-height:34px;color:var(--brand)}
.call-sub{font-size:14px;line-height:20px;color:var(--muted);margin-top:2px}
.follow-row{display:flex;justify-content:flex-end;align-items:center;gap:12px;margin-top:14px;font-size:14px;color:var(--brand)}
.social{display:flex;align-items:center;gap:5px;font-size:12px}
.social i{width:22px;height:22px;border-radius:50%;background:var(--brand);display:block}

.nav{left:101px;top:201px;width:951px;height:49px;border-radius:3px;background:linear-gradient(var(--nav-top),var(--nav-bottom));display:flex;list-style:none;overflow:hidden}
.nav li{height:49px;line-height:50px;color:#fff;font-size:14px;text-align:center;border-right:1px solid #35597e;box-shadow:1px 0 0 #6f98c0}
.nav li.active{background:linear-gradient(#86aed3,#5c87b1)}
.nav li:last-child{border:none;box-shadow:none}

.hero{left:101px;top:263px;width:950px;height:256px;border:1px solid #e6e6e6;box-shadow:0 0 3px rgba(0,0,0,.06)}
.hero-lead{left:194px;top:326px;font-size:23px;color:var(--brand)}
.hero-title{left:194px;top:363px;font-size:28px;color:var(--brand)}
.btn-dark{left:195px;top:412px;width:94px;height:32px;background:#3d3d3d;color:#fff;font-size:14px;text-align:center;line-height:32px;border-radius:2px}
.hero-visual{left:660px;top:272px;width:382px;height:239px;background:radial-gradient(ellipse at 60% 55%,#c9d8e8 0%,#e9eff5 45%,#fff 80%)}

.col-title{top:544px;font-size:20px;color:var(--brand)}
.dots{top:576px;width:262px;border-top:2px dotted #b9b9b9}
.divider{top:548px;width:1px;height:330px;background:#e3e3e3}
.more{top:852px;width:263px;height:27px;background:var(--strip);font-size:12px;color:var(--ink);text-align:right;padding:6px 8px 0 0}

.quote{left:103px;top:594px;width:264px;font-size:14px;font-weight:600;line-height:18px;text-align:justify}
.body-text{font-size:12.5px;line-height:22px;color:var(--ink);text-align:justify}

.services{left:446px;top:592px;list-style:none}
.services li{height:30px;font-size:13px;display:flex;align-items:center;gap:14px}

.video{left:790px;top:594px;width:262px;height:149px;background:#111;padding:3px}
.video-frame{width:256px;height:128px;background:linear-gradient(90deg,#3c3c3c,#6a6a6a 40%,#4a4a4a)}
.play{left:906px;top:651px;width:29px;height:19px;background:#111;border-radius:3px}
.video-bar{left:790px;top:726px;width:262px;height:17px;background:#222}

.news{left:93px;top:901px;width:966px;height:59px;background:var(--dark-band)}
.news-title{left:201px;top:918px;font-size:21px;color:#fff}
.news-input{left:334px;top:915px;width:250px;height:29px;background:#fff;border:1px solid #ccc;border-radius:2px;font-size:12px;font-style:italic;color:#999;padding:6px 12px}
.news-btn{left:597px;top:917px;width:68px;height:25px;background:linear-gradient(#f1dc8e,#c9a741);border-radius:2px;font-size:13px;font-weight:700;font-style:italic;color:#5b4a14;text-align:center;line-height:25px}
.news-copy{left:687px;top:922px;font-size:13px;color:#fff}

.footer{left:93px;top:960px;width:966px;height:87px;background:var(--footer)}
.foot-links{left:103px;top:975px;font-size:13px;color:#e5e5e5}
.foot-links span{margin:0 8px;color:#999}
.copyright{left:103px;top:1005px;font-size:13px;color:#e5e5e5}
.cards{left:877px;top:990px;display:flex;gap:8px}
.cards div{width:29px;height:19px;background:#f4f4f4;border-radius:2px;font-size:6.5px;color:#555;text-align:center;line-height:19px;font-weight:600}
</style>
</head>
<body>
<div class="stage">
  <div class="abs search">Search
    <svg width="12" height="12" viewBox="0 0 12 12"><circle cx="4.5" cy="4.5" r="3.3" fill="none" stroke="#888" stroke-width="1.4"/><line x1="7" y1="7" x2="11" y2="11" stroke="#888" stroke-width="1.6"/></svg>
  </div>

  <div class="abs sheet"></div>

  <div class="abs brand-name"><span class="dot"></span>BRENWICK VITALITY CLINIC</div>

  <svg class="abs call-icon" width="46" height="44" viewBox="0 0 46 44">
    <ellipse cx="23" cy="20" rx="20" ry="17" fill="#eef2f6" stroke="#b8c4d0" stroke-width="2"/>
    <path d="M14 12c2-3 5-3 6 0l1 3-3 2c1 3 3 5 6 6l2-3 3 1c3 1 3 4 0 6-5 3-17-7-15-15z" fill="#3f6a95"/>
  </svg>
  <div class="abs contact-block">
    <div class="call">Call (305) 555-0187</div>
    <div class="call-sub">for a Free Consultation with Dr. Brenwick</div>
    <div class="follow-row">Follow Us On:
      <span class="social"><i></i>Connectly</span>
      <span class="social"><i></i>Chirper</span>
    </div>
  </div>

  <ul class="abs nav">
    <li class="active" style="width:83px">HOME</li>
    <li style="width:111px">ABOUT US</li>
    <li style="width:178px">PRODUCTS / SERVICES</li>
    <li style="width:149px">HEALTH WISDOM</li>
    <li style="width:143px">APPOINTMENTS</li>
    <li style="width:90px">MEDIA</li>
    <li style="width:110px">CONTACT US</li>
  </ul>

  <div class="abs hero"></div>
  <div class="abs hero-lead">Brenwick Vitality Clinic specializes in</div>
  <div class="abs hero-title">OPTIMIZING YOUR HEALTH!</div>
  <div class="abs btn-dark">VIEW MORE</div>
  <div class="abs hero-visual" role="img" aria-label="Medical still life: stethoscope, vials, syringes and blue tablets"></div>

  <div class="abs col-title" style="left:103px">WELCOME</div>
  <div class="abs dots" style="left:103px"></div>
  <div class="abs col-title" style="left:446px">OUR SERVICES</div>
  <div class="abs dots" style="left:446px"></div>
  <div class="abs col-title" style="left:790px">WHAT WE DO</div>
  <div class="abs dots" style="left:790px"></div>
  <div class="abs divider" style="left:408px"></div>
  <div class="abs divider" style="left:750px"></div>

  <p class="abs quote">“A Doctor You Want to See…Dr. Brenwick goes beyond your average practitioner at Brenwick Vitality Clinic, taking a holistic view on traditional medicine.”</p>
  <p class="abs body-text" style="left:103px;top:676px;width:264px">Brenwick Vitality Clinic specializes in optimizing your health!</p>
  <p class="abs body-text" style="left:103px;top:742px;width:264px">We believe health, physical appearance, and mental well-being are all tied to what we consume, our environment, and ultimately, how we care for ourselves.</p>

  <ul class="abs services">
    <li><svg width="8" height="10"><path d="M1 1l5 4-5 4" fill="none" stroke="#777" stroke-width="2"/></svg>Anti-Aging Treatments</li>
    <li><svg width="8" height="10"><path d="M1 1l5 4-5 4" fill="none" stroke="#777" stroke-width="2"/></svg>Wellness-Lifecard Healthcare Program</li>
    <li><svg width="8" height="10"><path d="M1 1l5 4-5 4" fill="none" stroke="#777" stroke-width="2"/></svg>Weight Loss and Lifestyle Analysis</li>
    <li><svg width="8" height="10"><path d="M1 1l5 4-5 4" fill="none" stroke="#777" stroke-width="2"/></svg>Muscle and Joint Repair with (PRP)</li>
    <li><svg width="8" height="10"><path d="M1 1l5 4-5 4" fill="none" stroke="#777" stroke-width="2"/></svg>Laser Face-Lift</li>
    <li><svg width="8" height="10"><path d="M1 1l5 4-5 4" fill="none" stroke="#777" stroke-width="2"/></svg>Acne Treatment</li>
    <li><svg width="8" height="10"><path d="M1 1l5 4-5 4" fill="none" stroke="#777" stroke-width="2"/></svg>Cosmetic Injections</li>
    <li><svg width="8" height="10"><path d="M1 1l5 4-5 4" fill="none" stroke="#777" stroke-width="2"/></svg>Laser Hair Removal</li>
  </ul>

  <div class="abs video"><div class="video-frame" role="img" aria-label="Video still of the clinic's medical team"></div></div>
  <div class="abs video-bar">
    <svg width="262" height="17"><rect x="0" y="0" width="262" height="3" fill="#555"/><rect x="0" y="0" width="60" height="3" fill="#d22"/><circle cx="61" cy="2" r="3" fill="#eee"/><rect x="10" y="8" width="2" height="6" fill="#ccc"/><rect x="14" y="8" width="2" height="6" fill="#ccc"/></svg>
  </div>
  <div class="abs play"><svg width="29" height="19"><path d="M11 5l8 4.5-8 4.5z" fill="#fff"/></svg></div>
  <p class="abs body-text" style="left:789px;top:762px;width:263px">We believe health, physical appearance, and mental well-being are all tied to what we consume, our environment.</p>

  <div class="abs more" style="left:104px">View more</div>
  <div class="abs more" style="left:447px">View more</div>
  <div class="abs more" style="left:791px">View more</div>

  <div class="abs news"></div>
  <svg class="abs" style="left:160px;top:914px" width="30" height="30" viewBox="0 0 30 30"><path d="M3 12l12-9 12 9v14H3z" fill="#e9cf78"/><path d="M3 12l12 8 12-8" fill="none" stroke="#b8953b" stroke-width="1.5"/></svg>
  <div class="abs news-title">NEWSLETTER</div>
  <div class="abs news-input">Enter your mail ID</div>
  <div class="abs news-btn">SUBMIT</div>
  <div class="abs news-copy">Nam libero tempore, cum soluta nobis est eligendi optio</div>

  <div class="abs footer"></div>
  <div class="abs foot-links">Home<span>|</span>About us<span>|</span>Products / Services<span>|</span>Health Wisdom<span>|</span>Appointments<span>|</span>Media<span>|</span>Contact us</div>
  <div class="abs copyright">Copyright © 2012 www.brenvitale-example.com &nbsp;&nbsp;&nbsp;&nbsp;All rights reserved.</div>
  <div class="abs cards"><div>Paywell</div><div>Cardex</div><div>Mundo</div><div>Checkly</div><div>Vesta</div></div>
</div>
</body>
</html>
```